Online Dating Website called WinkAtWheel.com

PLEASE CAN ALL PARTICIPATING DESIGNERS PLEASE SUBMIT ALL PAGES AS DETAILED IN THE ORIGINAL BRIEF BELOW WITHIN 48 HOURS TO AVOID WINKATWHEEL EXTENDING THE CONTEST FURTHER.

We have an online dating website that is 95% fully functional and now require an exciting and creative designer to help us create the best dating experience. We are looking for your ideas on a couple of our key pages. These are our landing, profile and search page. We already have a homepage that we are happy with and winning designers will look to build upon the foundations of the homepage and extend them through their designs.

The premise of the site is the idea that if you've ever seen someone out driving and wished you could communicate because you found them attractive, how would you? Well with WinkAtWheel.com you can. Just enter their vehicle registration number (license plate) in to the website in order to get in touch, flirt and develop a relationship. It also allows users to find each other based on other criteria. It acts as both a specialist service and a normal dating website.

The pages that require developing are 1) our landing page, this is the page users see when they first login to the site, it comprises various pieces of information but it's primary function is a live feed of events generated based on the users favourited profiles and interactions with the user. 2) The profile page is the page where users can edit their own information, given the nature of this page we are looking for a creative design that gives this page some flair. 3) Finally we are looking for ideas for our search page, this page needs to provide a list of users who meet the user's search requirements and display the profile of a selected user.

Reason: We've asked for certain pages in our brief to be designed and this still hasn't been done. We've contacted the designers that have currently submitted designs and requested this several times. We still await for this to happen.

Target Market(s)

Male or Female age 18+

Industry/Entity Type

Dating

Requirements
Must have
• Our must have feature is a designer with an open mind. The functionality of the site must be present, all we ask is for you to be creative with the layout. Think out side of the box, change the colours, the layout, and the background as you feel. Make it look current and appealing to the user.
Nice to have
• Theme's carried through from the home page
Should not have
• Do not include Comic Sans or Times New Roman font in your designs.

```html
<!DOCTYPE html>
<html lang="en">
<head>
<meta charset="utf-8">
<title>WinkAtWheel.com – Live Feed</title>
<link href="https://fonts.googleapis.com/css2?family=Arimo:wght@400;700&family=Open+Sans:wght@400;700&display=swap" rel="stylesheet">
<style>
  :root{
    --page-green:#2f500f;
    --panel-bg:#efefef;
    --panel-frame:#ffffff;
    --rule:#d6d6d6;
    --ink:#333333;
    --ink-soft:#4a4a4a;
    --status-pink:#ff0a84;
    --date-navy:#17385a;
    --like-green:#7cc653;
    --btn-green-top:#a6d521;
    --btn-green-bottom:#5d9a0c;
    --btn-blue-top:#7fd0f5;
    --btn-blue-bottom:#1d95d8;
    --btn-text:#1f3b4d;
    --footer-top:#17181f;
    --footer-bottom:#3c3d42;
    --footer-text:#ffffff;
    --bubble-blue:#3c7cc1;
  }
  *{box-sizing:border-box;margin:0;padding:0}
  html,body{width:909px;height:1200px;overflow:hidden;background:var(--page-green)}
  .stage{position:relative;width:770px;height:1016px;transform:scale(1.18052);transform-origin:0 0;
    font-family:"Arimo",Arial,sans-serif;color:var(--ink);
    background:linear-gradient(var(--page-green) 0 850px,var(--footer-top) 850px,var(--footer-bottom) 1016px)}
  .panel{position:absolute;background:var(--panel-bg);border:3px solid var(--panel-frame);box-shadow:0 0 3px rgba(0,0,0,.35)}
  .pill{display:block;height:25px;line-height:25px;text-align:center;font-weight:700;font-size:13px;color:var(--btn-text);border-radius:2px;letter-spacing:.2px}
  .pill--green{background:linear-gradient(var(--btn-green-top),var(--btn-green-bottom))}
  .pill--blue{background:linear-gradient(var(--btn-blue-top),var(--btn-blue-bottom));border:1px solid #1a7fb8}

  /* feed filter */
  .filter{left:16px;top:18px;width:186px;height:354px;padding:9px 7px}
  .filter-group{padding:9px 6px 8px;border-bottom:1px solid var(--rule)}
  .filter-group:last-child{border-bottom:0}
  .filter-group h3{font-size:11.5px;font-weight:700;margin-bottom:6px;color:#2a2a2a}
  .filter-group li{list-style:none;font-size:9.5px;line-height:14px;color:var(--ink-soft)}

  /* favourites */
  .favourites{left:16px;top:388px;width:186px;height:426px;padding:8px 7px}
  .fav-search{display:flex;gap:4px;margin:7px 0 12px}
  .fav-search .field{width:96px;height:21px;background:#fff;border:1px solid #c9c9c9;font-size:9.5px;line-height:19px;padding-left:6px;color:#555}
  .fav-search .go{width:66px;height:21px;line-height:19px;font-size:11px;font-weight:400}
  .fav{display:flex;gap:6px;height:83px;padding-top:2px;border-bottom:1px solid var(--rule);margin:0 0 0 0}
  .fav + .fav{padding-top:14px}
  .fav-name{font-size:11px;font-weight:700;color:#222;margin-bottom:1px}
  .fav-meta{font-size:9.5px;line-height:14px;color:var(--ink-soft)}

  .photo{flex:none;width:62px;height:52px;background:#fff;border:1px solid #c4c4c4;padding:3px;box-shadow:0 1px 2px rgba(0,0,0,.2)}
  .photo span{display:block;width:100%;height:100%;background:linear-gradient(135deg,#c9e0ea 0%,#a8563a 45%,#e6c0a4 70%,#5b7f9e 100%)}

  /* feed */
  .card{position:absolute;left:210px;width:354px;background:var(--panel-bg);border:3px solid var(--panel-frame);box-shadow:0 0 3px rgba(0,0,0,.35);padding:4px 4px 0}
  .card-title{height:25px;line-height:25px;background:var(--status-pink);color:#fff;font-weight:700;font-size:13px;padding-left:13px}
  .card-body{display:flex;gap:9px;margin-top:8px;padding-left:1px}
  .card-body .photo{width:68px;height:53px}
  .card-text{font-size:9.5px;line-height:14px;color:var(--ink);padding-top:4px}
  .card-date{font-size:9.5px;color:var(--date-navy);margin:9px 0 0 1px}
  .card-like{font-size:9px;color:var(--like-green);margin:5px 0 0 4px;display:flex;align-items:center;gap:3px}

  /* backgrounds */
  .backgrounds{left:573px;top:3px;width:186px;height:267px;padding:7px 6px}
  .swatches{display:grid;grid-template-columns:repeat(3,51px);gap:8px 7px;margin-top:10px;padding-left:2px}
  .swatch{height:46px;border:2px solid #fff;box-shadow:0 0 2px rgba(0,0,0,.4)}

  /* footer */
  .footer{position:absolute;left:0;top:850px;width:770px;height:166px;font-family:"Open Sans",Arial,sans-serif;color:var(--footer-text)}
  .foot-col{position:absolute;top:34px;font-size:9.5px}
  .foot-col h4{font-size:9.5px;font-weight:700;margin-bottom:14px}
  .foot-col li{list-style:none;line-height:13.3px}
  .copyright{position:absolute;left:10px;top:130px;font-size:9.5px}
  .tweet{position:absolute;left:459px;top:35px;width:259px;height:43px;background:var(--bubble-blue);border-radius:5px;font-size:9px;padding:11px 8px}
  .tweet svg{position:absolute;left:212px;top:42px}
  .social{position:absolute;top:106px;font-size:10px;display:flex;align-items:center;gap:4px}
  .dot{width:6px;height:6px;background:#fff;display:inline-block}
</style>
</head>
<body>
<div class="stage">

  <section class="panel filter">
    <span class="pill pill--green">FEED FILTER</span>
    <div class="filter-group"><h3>STATUS UPDATES</h3><ul><li>Statuses by others</li><li>Statuses by me</li></ul></div>
    <div class="filter-group"><h3>IMAGE UPLOADS</h3><ul><li>Uploads by others</li><li>Uploads by me</li></ul></div>
    <div class="filter-group"><h3>PROFILE UPDATES</h3><ul><li>Updates by otheeres</li><li>Updates By Me</li><li>Image changes by others</li><li>Image changes by me</li></ul></div>
    <div class="filter-group"><h3>OTHERS</h3><ul><li>Received Messages</li><li>Views</li><li>favouring</li></ul></div>
  </section>

  <section class="panel favourites">
    <span class="pill pill--blue">YOUR FAVOURITES</span>
    <div class="fav-search"><div class="field">Type a name..</div><span class="pill pill--blue go">Search</span></div>
    <div class="fav"><div class="photo"><span role="img" aria-label="Member profile photo"></span></div><div><p class="fav-name">Kirsty</p><p class="fav-meta">22 years old<br>Leeds</p></div></div>
    <div class="fav"><div class="photo"><span role="img" aria-label="Member profile photo"></span></div><div><p class="fav-name">Kirsty</p><p class="fav-meta">22 years old<br>Leeds</p></div></div>
    <div class="fav"><div class="photo"><span role="img" aria-label="Member profile photo"></span></div><div><p class="fav-name">Kirsty</p><p class="fav-meta">22 years old<br>Leeds</p></div></div>
    <div class="fav"><div class="photo"><span role="img" aria-label="Member profile photo"></span></div><div><p class="fav-name">Kirsty</p><p class="fav-meta">22 years old<br>Leeds</p></div></div>
  </section>

  <!-- partially scrolled card at top -->
  <article class="card" style="top:-55px;height:133px">
    <div class="card-title">Lady changed her status</div>
    <div class="card-body"><div class="photo"><span role="img" aria-label="Member profile photo"></span></div><p class="card-text">Lorem ipsum dolor sit amet, consectetur adipiscing elit.<br>Maecenas fermentum ante id pellentesque consequat.</p></div>
    <p class="card-date">TuesDay 22:37</p>
    <p class="card-like"><svg width="8" height="7" viewBox="0 0 8 7"><path d="M4 7L.6 3.6A1.9 1.9 0 013.6.8L4 1.2l.4-.4a1.9 1.9 0 013 2.8z" fill="currentColor"/></svg>Like</p>
  </article>

  <article class="card" style="top:91px;height:133px">
    <div class="card-title">Lady changed her status</div>
    <div class="card-body"><div class="photo"><span role="img" aria-label="Member profile photo"></span></div><p class="card-text">Lorem ipsum dolor sit amet, consectetur adipiscing elit.<br>Maecenas fermentum ante id pellentesque consequat.</p></div>
    <p class="card-date">TuesDay 22:37</p>
    <p class="card-like"><svg width="8" height="7" viewBox="0 0 8 7"><path d="M4 7L.6 3.6A1.9 1.9 0 013.6.8L4 1.2l.4-.4a1.9 1.9 0 013 2.8z" fill="currentColor"/></svg>Like</p>
  </article>

  <article class="card" style="top:238px;height:133px">
    <div class="card-title">Lady changed her status</div>
    <div class="card-body"><div class="photo"><span role="img" aria-label="Member profile photo"></span></div><p class="card-text">Lorem ipsum dolor sit amet, consectetur adipiscing elit.<br>Maecenas fermentum ante id pellentesque consequat.</p></div>
    <p class="card-date">TuesDay 22:37</p>
    <p class="card-like"><svg width="8" height="7" viewBox="0 0 8 7"><path d="M4 7L.6 3.6A1.9 1.9 0 013.6.8L4 1.2l.4-.4a1.9 1.9 0 013 2.8z" fill="currentColor"/></svg>Like</p>
  </article>

  <article class="card" style="top:384px;height:135px">
    <div class="card-title">Lady changed her status</div>
    <div class="card-body"><div class="photo"><span role="img" aria-label="Member profile photo"></span></div><p class="card-text">Lorem ipsum dolor sit amet, consectetur adipiscing elit.<br>Maecenas fermentum ante id pellentesque consequat.</p></div>
    <p class="card-date">TuesDay 22:37</p>
    <p class="card-like"><svg width="8" height="7" viewBox="0 0 8 7"><path d="M4 7L.6 3.6A1.9 1.9 0 013.6.8L4 1.2l.4-.4a1.9 1.9 0 013 2.8z" fill="currentColor"/></svg>Like</p>
  </article>

  <article class="card" style="top:531px;height:135px">
    <div class="card-title">Lady changed her status</div>
    <div class="card-body"><div class="photo"><span role="img" aria-label="Member profile photo"></span></div><p class="card-text">Lorem ipsum dolor sit amet, consectetur adipiscing elit.<br>Maecenas fermentum ante id pellentesque consequat.</p></div>
    <p class="card-date">TuesDay 22:37</p>
    <p class="card-like"><svg width="8" height="7" viewBox="0 0 8 7"><path d="M4 7L.6 3.6A1.9 1.9 0 013.6.8L4 1.2l.4-.4a1.9 1.9 0 013 2.8z" fill="currentColor"/></svg>Like</p>
  </article>

  <article class="card" style="top:678px;height:135px">
    <div class="card-title">Lady changed her status</div>
    <div class="card-body"><div class="photo"><span role="img" aria-label="Member profile photo"></span></div><p class="card-text">Lorem ipsum dolor sit amet, consectetur adipiscing elit.<br>Maecenas fermentum ante id pellentesque consequat.</p></div>
    <p class="card-date">TuesDay 22:37</p>
    <p class="card-like"><svg width="8" height="7" viewBox="0 0 8 7"><path d="M4 7L.6 3.6A1.9 1.9 0 013.6.8L4 1.2l.4-.4a1.9 1.9 0 013 2.8z" fill="currentColor"/></svg>Like</p>
  </article>

  <section class="panel backgrounds">
    <span class="pill pill--blue">BACKGROUND SELECT</span>
    <div class="swatches">
      <div class="swatch" role="img" aria-label="Teal textured background" style="background:linear-gradient(135deg,#1f5f6c,#2d7380)"></div>
      <div class="swatch" role="img" aria-label="Green bokeh background" style="background:linear-gradient(135deg,#c6e08a,#6fae2e)"></div>
      <div class="swatch" role="img" aria-label="Night sky background" style="background:radial-gradient(circle at 60% 40%,#5b4aa0,#120f3a)"></div>
      <div class="swatch" role="img" aria-label="Sunburst background" style="background:radial-gradient(circle at 30% 25%,#ffd23a,#f6e6a8 55%,#d8eef4)"></div>
      <div class="swatch" role="img" aria-label="Blue light waves background" style="background:linear-gradient(160deg,#071a4a,#1f5fc8 55%,#0a1f55)"></div>
      <div class="swatch" role="img" aria-label="Sky with clouds background" style="background:linear-gradient(#19b3e6,#6ad2f2)"></div>
      <div class="swatch" role="img" aria-label="Wood grain background" style="background:linear-gradient(90deg,#8a8b86,#b8b6ac,#7a7a74,#aaa89e)"></div>
      <div class="swatch" role="img" aria-label="Teal light rays background" style="background:linear-gradient(135deg,#3a8d9e,#1b5364)"></div>
      <div class="swatch" role="img" aria-label="Pale green pattern background" style="background:linear-gradient(135deg,#e2e4a6,#cfd48a)"></div>
      <div class="swatch" role="img" aria-label="Green bubbles background" style="background:radial-gradient(circle,#3fc23a,#138a1c)"></div>
      <div class="swatch" role="img" aria-label="Wooden planks background" style="background:linear-gradient(#a88a63,#6e5236)"></div>
      <div class="swatch" role="img" aria-label="Abstract green swirl background" style="background:linear-gradient(135deg,#eaf7e2,#5fc58a 55%,#d8f0c8)"></div>
    </div>
  </section>

  <footer class="footer">
    <div class="foot-col" style="left:10px"><h4>WinkAtWheel.com</h4><ul><li>Homepage</li><li>Mobile Site</li><li>Friendbook</li><li>Chirper</li></ul></div>
    <div class="foot-col" style="left:158px"><h4>Legal</h4><ul><li>General Conditions</li><li>Terms &amp; Conditions</li><li>Privacy Statement</li><li>Cookies Information</li></ul></div>
    <div class="foot-col" style="left:306px"><h4>Support</h4><ul><li>Contact Us</li><li>FAQ's &amp; Help</li><li>Safe Dating Advice</li><li>Pricing Details</li></ul></div>
    <div class="tweet">Unable to connect to Chirper at this time.
      <svg width="14" height="12" viewBox="0 0 14 12"><path d="M0 0H14L12 12Z" fill="var(--bubble-blue)"/></svg>
    </div>
    <p class="social" style="left:488px"><span class="dot"></span>Like us on Friendbook</p>
    <p class="social" style="left:606px"><span class="dot"></span>Follow us on Chirper</p>
    <p class="copyright">©2013 WinkAtWheel.com, All Rights Reserved</p>
  </footer>

</div>
</body>
</html>
```